New High End Wine Lable- Our company is introducing our New High end vintage of wine

I need a elegant classy rear and front wine label designed

The labels must be black and gold.

Rear Label

-Must have The Below Text)
Our family is of Italian heritage, wine making and grape growing is in our blood. When our family migrated to Australia one of the first things they done was plant grape vines to remind them of their home back in Italy. Our vines are over 50 years old and our original vineyard is located in the Adelaide hills of South Australia.

We are the 3rd generation of Australian/Italian wine producers and want to showcase the traditions of Italian wine making using the clean environment of Australia

Produced by
Morvale Ridge Wines
4, 219 Upper Kestrel Bend Road
Lindfarrow, SA 5091
www.morvaleridgewines.example
8.6 Standard Drinks
14.5% Alc Vol
Contains Sulphites
750ml Net Content

- Also Must have space for a bar code
-Also must have space for a QR code

Front Label

Designers own expression of design and shape
Only requirements are:
-name of Brand "Morvale Ridge 89"'
- the Text "Wine of Australia"
-and Text "2013 Shiraz"

Industry/Entity Type

Environment

Font styles to use
Decorative

Requirements
Must have
• Black and Gold
• Eye Catching
• Expensive looking
• Front and Rear Label

```html
<!DOCTYPE html>
<html lang="en">
<head>
<meta charset="utf-8">
<title>Morvale Ridge 89 – Wine Labels</title>
<link rel="stylesheet" href="https://fonts.googleapis.com/css2?family=Della+Respira&family=Pinyon+Script&family=Cormorant+Garamond:wght@500;600&display=swap">
<style>
  :root {
    --backdrop: #0f0d0e;
    --backdrop-low: #2a0d14;
    --gold: #c9a437;
    --gold-light: #dcbc55;
    --gold-deep: #a9852a;
    --ink: #141211;
    --panel: #151413;
  }
  * { box-sizing: border-box; margin: 0; padding: 0; }
  html, body { width: 1200px; height: 974px; overflow: hidden; }
  body {
    background: radial-gradient(ellipse at 50% 100%, var(--backdrop-low) 0%, var(--backdrop) 60%);
    display: flex;
    align-items: center;
    justify-content: center;
    gap: 80px;
  }

  /* Front label */
  .front-label {
    position: relative;
    width: 440px;
    height: 620px;
  }
  .front-label .vineyard-art {
    position: absolute;
    inset: 0;
    background: linear-gradient(180deg, var(--gold) 0%, var(--gold-light) 45%, var(--gold-deep) 100%);
  }
  .cartouche {
    position: absolute;
    left: 50%;
    top: 50%;
    transform: translate(-50%, -54%);
    width: 340px;
    height: 300px;
    border: 3px solid var(--ink);
    border-radius: 90px / 60px;
    background: var(--gold-light);
    box-shadow: 0 0 0 6px var(--gold-light), 0 0 0 8px var(--ink);
    text-align: center;
    color: var(--ink);
    display: flex;
    flex-direction: column;
    align-items: center;
    justify-content: center;
  }
  .vintage {
    font-family: "Pinyon Script", cursive;
    font-size: 38px;
    line-height: 1;
    margin-bottom: 28px;
  }
  .brand-name {
    font-family: "Della Respira", serif;
    font-weight: 400;
    font-size: 38px;
    line-height: 1.1;
    padding: 10px 0;
    border-top: 1.5px solid var(--ink);
    border-bottom: 1.5px solid var(--ink);
  }
  .origin {
    font-family: "Della Respira", serif;
    font-size: 20px;
    margin-top: 28px;
  }

  /* Rear label */
  .rear-label {
    position: relative;
    width: 440px;
    height: 620px;
    padding: 22px;
  }
  .rear-label .border-art {
    position: absolute;
    inset: 0;
    background: linear-gradient(135deg, var(--gold-light), var(--gold-deep));
  }
  .rear-panel {
    position: relative;
    height: 100%;
    background: var(--panel);
    color: var(--gold);
    font-family: "Cormorant Garamond", serif;
    font-weight: 500;
    padding: 22px 24px;
    display: flex;
    flex-direction: column;
    gap: 14px;
  }
  .stats {
    display: grid;
    grid-template-columns: 1fr 1fr;
    row-gap: 4px;
  }
  .caption { font-size: 13px; line-height: 1.2; }
  .figure-large { font-family: "Della Respira", serif; font-size: 36px; line-height: 1.05; }
  .figure-mid { font-family: "Della Respira", serif; font-size: 30px; line-height: 1; }
  .drinks { display: flex; align-items: center; gap: 12px; }
  .align-right { text-align: right; }

  .origin-row {
    display: flex;
    align-items: center;
    justify-content: space-between;
  }
  .wine-origin { font-size: 17px; }
  .map-area {
    width: 78px;
    height: 64px;
    border-radius: 40% 50% 45% 35%;
    background: radial-gradient(circle at 50% 45%, var(--gold-light), var(--gold));
  }

  .heritage {
    font-size: 11.5px;
    line-height: 1.35;
    text-align: justify;
  }
  .heritage p + p { margin-top: 6px; }

  .footer-row {
    margin-top: auto;
    display: flex;
    align-items: flex-end;
    justify-content: space-between;
    gap: 12px;
  }
  .producer {
    font-size: 12px;
    line-height: 1.3;
  }
  .code-spaces {
    display: flex;
    align-items: flex-end;
    gap: 10px;
  }
  .qr-space {
    width: 62px;
    height: 62px;
    border: 1px dashed var(--gold);
  }
  .barcode-space {
    width: 96px;
    height: 52px;
    border: 1px dashed var(--gold);
  }
</style>
</head>
<body>

  <section class="front-label" aria-label="Front label">
    <div class="vineyard-art" role="img" aria-label="Gold and black line illustration of grape vines and rolling vineyard rows"></div>
    <div class="cartouche">
      <p class="vintage">2013 Shiraz</p>
      <h1 class="brand-name">Morvale Ridge 89</h1>
      <p class="origin">Wine of Australia</p>
    </div>
  </section>

  <section class="rear-label" aria-label="Rear label">
    <div class="border-art" role="img" aria-label="Gold border illustration of grape vines"></div>
    <div class="rear-panel">
      <div class="stats">
        <div>
          <p class="caption">Net Content</p>
          <p class="figure-large">750ml</p>
        </div>
        <div class="align-right">
          <p class="caption">Alcohol/Volume</p>
          <p class="figure-large">14.5%</p>
        </div>
        <div class="drinks">
          <p class="caption">Approx<br>Standard Drinks</p>
          <p class="figure-mid">8.6</p>
        </div>
        <p class="caption align-right">Contains Sulphites</p>
      </div>

      <div class="origin-row">
        <p class="wine-origin">Wine of Australia</p>
        <div class="map-area" role="img" aria-label="Gold map of Australia"></div>
      </div>

      <div class="heritage">
        <p>Our family is of Italian heritage, wine making and grape growing is in our blood. When our family migrated to Australia one of the first things they done was plant grape vines to remind them of their home back in Italy. Our vines are over 50 years old and our original vineyard is located in the Adelaide hills of South Australia.</p>
        <p>We are the 3rd generation of Australian/Italian wine producers and want to showcase the traditions of Italian wine making using the clean environment of Australia.</p>
      </div>

      <div class="footer-row">
        <div class="producer">
          <p>Produced by</p>
          <p>Morvale Ridge Wines</p>
          <p>4, 219 Upper Kestrel Bend Road</p>
          <p>Lindfarrow, SA 5091</p>
          <p>www.morvaleridgewines.example</p>
        </div>
        <div class="code-spaces">
          <div class="qr-space" role="img" aria-label="Space reserved for QR code"></div>
          <div class="barcode-space" role="img" aria-label="Space reserved for barcode"></div>
        </div>
      </div>
    </div>
  </section>

</body>
</html>
```